Business Card Design Project

Im an electrician and my company name is Kestrel Electrical
My main work is installing Lighting and Power Points, Home Theater Systems, TVS, Phones and Data
Im looking a business card, something nice, clean, modern and not to cluttered
Im open to sugestions
I dont mind if the "Services" is on the back on the business card
colours black, grey, white or the blue colour of my logo are prefered but not compulsory
any questions just message me
and please make it so if i need to edit the writing can do it easy. maybe by making it a seperate layer ?
My Details are.
Name - Peter Halloran
Job Title - Licenced Electrician
Mobile - 027 583 2174
Email - peter@kestrelelectrical.co.nz
Web - www.kestrelelectrical.co.nz
Services
Residential / Commercial
Lighting & Power
Heating & Ventilation
Automation
Phone & Data
Home Cinema
Sound Systems
TV, Antenna & Satellite
Digital Upgrades

```html
<!DOCTYPE html>
<html lang="en">
<head>
<meta charset="utf-8">
<title>Kestrel Electrical – Business Card</title>
<link href="https://fonts.googleapis.com/css2?family=Oswald:wght@400;500;600&display=swap" rel="stylesheet">
<style>
  :root {
    --card-yellow: #fbe733;
    --bar-black: #1d1d1b;
    --brand-blue: #4eabc9;
    --page-white: #ffffff;
  }
  html, body {
    margin: 0;
    padding: 0;
    width: 1200px;
    height: 1000px;
    overflow: hidden;
    background: var(--page-white);
  }
  .canvas {
    position: relative;
    width: 1200px;
    height: 1000px;
  }
  .card {
    position: absolute;
    width: 552px;
    height: 315px;
    background: var(--card-yellow);
  }
  .card--front { left: 95px; top: 148px; }
  .card--back { left: 549px; top: 536px; }

  /* Brand name block */
  .brand {
    position: absolute;
    left: 63px;
    top: 42px;
    display: flex;
    align-items: center;
    gap: 22px;
  }
  .brand__square {
    width: 70px;
    height: 70px;
    background: var(--brand-blue);
  }
  .brand__name {
    margin: 0;
    font-family: "Oswald", sans-serif;
    font-weight: 500;
    font-size: 46px;
    line-height: 1.02;
    letter-spacing: 3px;
    color: var(--brand-blue);
    text-transform: uppercase;
  }

  /* Service bars */
  .service-bar {
    position: absolute;
    left: 62px;
    width: 427px;
    height: 27px;
    background: var(--bar-black);
    color: var(--card-yellow);
    font-family: "Oswald", sans-serif;
    font-weight: 600;
    font-size: 15px;
    letter-spacing: 0.3px;
    line-height: 27px;
    text-align: center;
    margin: 0;
  }
  .service-bar--primary { top: 200px; }
  .service-bar--secondary { top: 254px; }

  /* Contact rows */
  .contact-list {
    list-style: none;
    margin: 0;
    padding: 0;
  }
  .contact-row {
    position: absolute;
    left: 134px;
    width: 287px;
    height: 26px;
    background: var(--bar-black);
    color: var(--card-yellow);
    font-family: "Oswald", sans-serif;
    font-weight: 400;
    font-size: 17px;
    line-height: 26px;
    display: flex;
    align-items: center;
  }
  .contact-row__icon {
    width: 20px;
    height: 16px;
    margin-left: 11px;
    margin-right: 10px;
    fill: var(--card-yellow);
    flex: none;
  }
  .contact-row--name { top: 44px; }
  .contact-row--role { top: 96px; }
  .contact-row--phone { top: 148px; }
  .contact-row--email { top: 201px; text-transform: uppercase; }
  .contact-row--web { top: 254px; text-transform: uppercase; }
</style>
</head>
<body>
<main class="canvas">

  <section class="card card--front" aria-label="Card front">
    <div class="brand">
      <div class="brand__square"></div>
      <h1 class="brand__name">Kestrel<br>Electrical</h1>
    </div>
    <p class="service-bar service-bar--primary">Lighting | Power Points | Home Theater Systems</p>
    <p class="service-bar service-bar--secondary">TV’s | Phones | Data</p>
  </section>

  <section class="card card--back" aria-label="Card back">
    <ul class="contact-list">
      <li class="contact-row contact-row--name">
        <svg class="contact-row__icon" viewBox="0 0 20 16" aria-hidden="true">
          <circle cx="10" cy="4.5" r="4"/>
          <path d="M2 16 Q2 9 10 9 Q18 9 18 16 Z"/>
        </svg>
        Peter Halloran
      </li>
      <li class="contact-row contact-row--role">
        <svg class="contact-row__icon" viewBox="0 0 20 16" aria-hidden="true">
          <path d="M8 0 H13 L11 6 H15 L7 16 L9 8 H5 Z"/>
        </svg>
        Licenced Electrician
      </li>
      <li class="contact-row contact-row--phone">
        <svg class="contact-row__icon" viewBox="0 0 20 16" aria-hidden="true">
          <path d="M7 2 H13 Q14 2 14 3 V15 Q14 16 13 16 H7 Q6 16 6 15 V3 Q6 2 7 2 Z M8 4 V9 H12 V4 Z"/>
          <rect x="11" y="0" width="1.4" height="3"/>
        </svg>
        027 583 2174
      </li>
      <li class="contact-row contact-row--email">
        <svg class="contact-row__icon" viewBox="0 0 20 16" aria-hidden="true">
          <path d="M0 2 H20 V15 H0 Z M2 4 V13 H18 V4 L10 10 Z M3.5 3.5 L10 8 L16.5 3.5 Z" fill-rule="evenodd"/>
        </svg>
        peter@kestrelelectrical.co.nz
      </li>
      <li class="contact-row contact-row--web">
        <svg class="contact-row__icon" viewBox="0 0 20 16" aria-hidden="true">
          <path d="M10 1 L19 8.5 L17.8 9.8 L10 3.4 L2.2 9.8 L1 8.5 Z"/>
          <path d="M4 9.5 L10 4.6 L16 9.5 V16 H12 V11 H8 V16 H4 Z"/>
        </svg>
        www.kestrelelectrical.co.nz
      </li>
    </ul>
  </section>

</main>
</body>
</html>
```